Moonlit Cadence - lifestyle coaching for women looking for D/s dynamic

Create website design and logo based on the requirements in the creative brief file.

Executive summary:
Company Info
Moonlit Cadence is a new life and intimacy coaching company founded by a life and fitness coach. The company focuses on integrating power exchange dynamics into intimate relationships, based on the founder’s personal journey.

Product
The company offers subscription-based online coaching programs with online class structure provided through a learning management system.
Customer Profile
• Target Audience: Women aged 45-55
• Customer needs: see appendix 1
• Language: English-speaking
• Economic Status: Middle to upper class
• Device Usage: Predominantly mobile (iOS and Android)

Target Market(s)

• Target Audience: Women aged 45-55 • Customer needs: see appendix 1 • Language: English-speaking • Economic Status: Middle to upper class • Device Usage: Predominantly mobile (iOS and Android)

Industry/Entity Type

Personal Development / Lifestyle Coaching

Coding

Coded - Design and coding required

Number of Pages Required

1 page

Font styles to use
Sans Serif

Requirements
Must have
• Lead capture tools, scheduling of intake calls, payment via Stripe, ready to be maintained by WIX or Wordpress
Nice to have
• Blog page

```html
<!DOCTYPE html>
<html lang="en">
<head>
<meta charset="utf-8">
<title>Moonlit Cadence</title>
<link rel="stylesheet" href="https://fonts.googleapis.com/css2?family=Cormorant+Garamond:ital,wght@0,300;0,400;1,300;1,400&family=Poppins:wght@300;400;500&display=swap">
<style>
:root{
  --ink:#2b2b2b;
  --muted:#6d6d6d;
  --teal:#3e5d5a;
  --charcoal:#3a3a3a;
  --gold-1:#d8bb83;
  --gold-2:#a9864c;
  --paper:#ffffff;
  --line:#cfcfcf;
}
*{box-sizing:border-box;margin:0;padding:0}
html,body{width:1200px;height:4196px;overflow:hidden;background:var(--paper)}
body{font-family:"Poppins",sans-serif;color:var(--ink);position:relative}
.serif{font-family:"Cormorant Garamond",serif;font-weight:300}
em{font-style:italic}
.abs{position:absolute}
.btn{display:inline-block;font-family:"Poppins",sans-serif;font-size:11px;font-weight:400;color:#2b2b2b;
  padding:11px 28px;border-radius:30px;background:linear-gradient(90deg,var(--gold-1),var(--gold-2));text-decoration:none;white-space:nowrap}
.btn-outline{background:#fff;border:1px solid #bbb;color:#444}

/* header */
.site-header{left:0;top:0;width:1200px;height:67px;display:flex;align-items:center;justify-content:space-between;padding:0 88px}
.brand{font-weight:300;font-size:17px;letter-spacing:2px;text-transform:uppercase;color:var(--ink)}
.nav{display:flex;align-items:center;gap:46px;font-size:10.5px}
.nav a{color:var(--ink);text-decoration:none}
.nav .nav-cta{background:#2f2f2f;color:#fff;padding:8px 36px;border-radius:20px}

/* hero */
.hero-copy{left:88px;top:160px;width:470px}
.hero-title{font-size:56px;line-height:1.06}
.hero-welcome{font-size:11px;margin:28px 0 34px}
.hero-photo{left:525px;top:67px;width:675px;height:477px;
  background:linear-gradient(135deg,#e6e4df 0%,#cfccc5 40%,#4a4744 70%,#2f4a2d 100%)}

/* coaching */
.coach-photo-chair{left:268px;top:656px;width:323px;height:497px;background:linear-gradient(160deg,#f1f0ec,#b9a48a 60%,#6e5a44)}
.coach-photo-reader{left:92px;top:862px;width:245px;height:240px;background:linear-gradient(160deg,#8b7563,#3c302a 70%)}
.coach-title{left:400px;top:672px;width:660px;font-size:30px;line-height:1.25}
.coach-title .r{display:block;text-align:right}
.coach-list{left:724px;top:775px;width:320px}
.coach-item{height:120px}
.coach-item h4{font-size:11px;font-weight:500;margin:8px 0 7px}
.coach-item p{font-size:9px;line-height:1.6;color:var(--muted)}
.coach-btn{left:694px;top:1159px}

/* about */
.about-panel{left:87px;top:1275px;width:1025px;height:345px;background:var(--teal)}
.about-edge{left:87px;top:1612px}
.about-copy{left:148px;top:1340px;width:410px;color:#fff}
.about-copy h2{font-size:28px;margin-bottom:14px}
.about-copy p{font-size:8.6px;line-height:1.6;margin-bottom:9px;color:#e7ecea}
.about-photo{left:699px;top:1322px;width:324px;height:263px;background:linear-gradient(150deg,#bfc7c2,#7e8a86 60%,#5c6a66)}

.divider{left:434px;width:321px;height:2px;background:linear-gradient(90deg,#333 0 18%,transparent 18% 30%,var(--line) 30%)}

/* why */
.why-title{left:0;top:1780px;width:1200px;text-align:center;font-size:28px}
.why-lead{left:330px;top:1830px;width:540px;text-align:center;font-size:8.6px;line-height:1.6;color:var(--muted)}
.why-banner{left:87px;top:1894px;width:1025px;height:258px;background:linear-gradient(100deg,#d8b98a,#caa371 40%,#e3cfae 80%)}
.why-caption{left:87px;top:2133px;width:1025px;text-align:center;font-size:26px}
.feature{width:280px;text-align:center;top:2199px}
.feature h4{font-size:10.5px;font-weight:500;margin:8px 0 7px}
.feature p{font-size:8.6px;line-height:1.6;color:var(--muted)}
.why-btn{left:0;top:2361px;width:1200px;text-align:center}

/* testimonial */
.testi-photo{left:179px;top:2466px;width:408px;height:372px;background:linear-gradient(180deg,#b9d2e3 0%,#d7e3ea 45%,#5e86a0 60%,#8a6a4c 100%)}
.quote-mark{left:668px;top:2490px;font-size:48px;line-height:1}
.quote{left:670px;top:2540px;width:400px;font-size:18px;line-height:1.5}
.quote-by{left:670px;top:2795px;font-size:11px}

/* insights */
.ins-title{left:0;top:2996px;width:1200px;text-align:center;font-size:28px;line-height:1.15}
.ins-lead{left:0;top:3072px;width:1200px;text-align:center;font-size:8.6px;color:var(--muted)}
.post{text-align:center}
.post .thumb{margin:0 auto 18px}
.post h4{font-size:10.5px;font-weight:400;line-height:1.45;margin-bottom:7px}
.post p{font-size:8.6px;line-height:1.55;color:var(--muted);margin:0 auto 16px;width:240px}
.post .btn{font-size:9px;padding:9px 24px}

/* cta */
.cta-panel{left:87px;top:3640px;width:1025px;height:248px;background:var(--teal)}
.cta-edge{left:87px;top:3622px}
.cta-copy{left:146px;top:3690px;width:440px;color:#fff}
.cta-copy h2{font-size:27px;line-height:1.2;margin-bottom:22px}
.cta-photo{left:714px;top:3573px;width:378px;height:315px;background:linear-gradient(160deg,#2c2c2c,#1f1f1f 50%,#cdbba6)}

/* footer */
.footer{left:0;top:3888px;width:1200px;height:308px;background:var(--charcoal);color:#eee}
.f-col{top:100px}
.footer h5{font-size:9px;font-weight:500;margin-bottom:10px}
.footer ul{list-style:none}
.footer li{font-size:8.4px;line-height:1.8;color:#cfcfcf}
.footer .brand{color:#fff;font-size:16px}
.socials{display:flex;gap:8px;margin-top:16px}
.socials span{width:14px;height:14px;border-radius:50%;background:var(--gold-1)}
.contact li{display:flex;gap:7px;align-items:flex-start;margin-bottom:4px}
.contact svg{margin-top:4px;flex:none}
.subscribe p{font-size:8.4px;line-height:1.55;color:#cfcfcf;width:220px;margin-bottom:12px}
.sub-field{display:flex;width:205px;height:24px}
.sub-field span{flex:1;background:#fff;font-size:7px;color:#999;padding:7px 10px}
.sub-field b{width:30px;background:var(--gold-2);color:#fff;font-size:11px;text-align:center;line-height:24px;font-weight:400}
.footer-bottom{left:110px;top:262px;width:980px;display:flex;justify-content:space-between;font-size:7.5px;color:#cfcfcf}
.footer-bottom .gold{color:var(--gold-1)}
</style>
</head>
<body>

<header class="abs site-header">
  <div class="brand">Moonlit Cadence</div>
  <nav class="nav">
    <a href="#">Home</a><a href="#">About</a><a href="#">Services</a><a href="#">Testimonials</a><a href="#">Blog</a>
    <a href="#" class="nav-cta">Contact</a>
  </nav>
</header>

<div class="abs hero-photo" role="img" aria-label="Smiling blonde woman in a striped shirt seated by a white brick wall with green plants"></div>
<div class="abs hero-copy">
  <h1 class="hero-title serif">Unlock the<br>secrets of <em>new level</em><br>connection and<br>self-discovery.</h1>
  <p class="hero-welcome">Welcome, to Moonlit Cadence.</p>
  <a class="btn" href="#">Book Your Free 30-Minute Consultation</a>
</div>

<div class="abs coach-photo-chair" role="img" aria-label="Woven wooden chair beside a bright window"></div>
<div class="abs coach-photo-reader" role="img" aria-label="Woman in a dark blouse reading a book"></div>
<h2 class="abs coach-title serif">Tailored coaching for deeper connection <span class="r">and life changing <em>intimacy.</em></span></h2>
<div class="abs coach-list">
  <div class="coach-item">
    <svg width="20" height="20" viewBox="0 0 18 18" fill="none" stroke="#333" stroke-width="1"><circle cx="9" cy="9" r="7"/><circle cx="9" cy="9" r="3"/><path d="M9 2v4M9 12v4M2 9h4M12 9h4"/></svg>
    <h4>Rekindle &amp; Connect</h4>
    <p>A foundational program designed for couples seeking to reestablish intimacy and communication through structured power exchange exercises.</p>
  </div>
  <div class="coach-item">
    <svg width="20" height="20" viewBox="0 0 18 18" fill="none" stroke="#333" stroke-width="1"><circle cx="6" cy="10" r="4"/><circle cx="12" cy="10" r="4"/></svg>
    <h4>Deep Dive Relationship Coaching</h4>
    <p>For couples wanting to explore deeper power dynamics in their relationship and incorporate these practices into daily life for lasting fulfillment.</p>
  </div>
  <div class="coach-item">
    <svg width="20" height="20" viewBox="0 0 18 18" fill="none" stroke="#333" stroke-width="1"><circle cx="9" cy="6" r="3"/><path d="M3 16c0-4 3-6 6-6s6 2 6 6"/></svg>
    <h4>Self-Discovery</h4>
    <p>A one-on-one program for individuals seeking to understand and embrace power exchange dynamics as part of their personal journey toward self-empowerment.</p>
  </div>
</div>
<a class="abs btn coach-btn" href="#">Discover More!</a>

<div class="abs about-panel"></div>
<svg class="abs about-edge" width="1025" height="30" viewBox="0 0 1025 30"><path d="M0 0H1025V12L990 20 950 10 900 22 850 9 800 19 740 8 690 21 630 10 570 20 510 8 450 22 390 10 330 19 270 8 210 21 150 10 100 19 50 8 0 16Z" fill="#3e5d5a"/></svg>
<div class="abs about-copy">
  <h2 class="serif">About moonlit <em>cadence.</em></h2>
  <p>At Moonlit Cadence, we believe that intimacy and connection are key pillars of a fulfilling relationship and life. Founded by an experienced life and fitness coach, our mission is to empower individuals and couples to rediscover passion, confidence, and emotional connection in their relationships. We specialize in integrating power dynamics and self discovery into intimate relationships, providing a transformative journey of personal growth and fulfillment.</p>
  <p>With our online coaching programs, we offer practical tools and guidance that help our clients embrace their inner strength, overcome insecurities, and reignite the spark in their relationships.</p>
  <a class="btn" href="#" style="margin-top:8px;font-size:9.5px;padding:10px 24px">Discover More!</a>
</div>
<div class="abs about-photo" role="img" aria-label="Grey-haired woman in a soft knit cardigan outdoors"></div>

<div class="abs divider" style="top:1711px"></div>

<h2 class="abs why-title serif">Why choose moonlit <em>cadence?</em></h2>
<p class="abs why-lead">Our approach is rooted in calm confidence, personal empowerment, and creating a safe space for exploration. With programs tailored to your needs, we help women aged 45-55 rediscover themselves and their relationships in ways that feel aligned, comfortable, and exciting.</p>
<div class="abs why-banner" role="img" aria-label="Woman in white sitting against a warm sandstone wall beside green plants"></div>
<p class="abs why-caption serif">The moonlit cadence difference</p>
<div class="abs feature" style="left:107px">
  <svg width="20" height="20" viewBox="0 0 18 18" fill="none" stroke="#333" stroke-width="1"><circle cx="9" cy="9" r="7"/><path d="M5 9l3 3 5-6"/></svg>
  <h4>Personalized Coaching</h4>
  <p>Each program is tailored to meet your unique needs, helping you navigate your personal journey with the guidance of a trusted coach.</p>
</div>
<div class="abs feature" style="left:459px">
  <svg width="20" height="20" viewBox="0 0 18 18" fill="none" stroke="#333" stroke-width="1"><path d="M9 15S3 11 3 6.5A3 3 0 0 1 9 5a3 3 0 0 1 6 1.5C15 11 9 15 9 15Z"/></svg>
  <h4>Holistic Approach</h4>
  <p>We address both emotional and physical aspects of intimacy, focusing on self-confidence, communication, and connection.</p>
</div>
<div class="abs feature" style="left:816px">
  <svg width="20" height="20" viewBox="0 0 18 18" fill="none" stroke="#333" stroke-width="1"><circle cx="9" cy="5" r="2.5"/><circle cx="4" cy="12" r="2.5"/><circle cx="14" cy="12" r="2.5"/></svg>
  <h4>Supportive Community</h4>
  <p>We create a compassionate, non-judgmental space where you can explore, grow, and feel supported throughout your journey.</p>
</div>
<div class="abs why-btn"><a class="btn" href="#">Book Your Free 30-Minute Consultation</a></div>

<div class="abs testi-photo" role="img" aria-label="Wooden boardwalk leading toward a calm blue sea"></div>
<div class="abs quote-mark serif">”</div>
<p class="abs quote serif">After years of feeling disconnected in my marriage, Moonlit Cadence helped me rebuild not just my relationship, but my confidence in who I am. The coaching helped me and my partner explore new sides of our relationship we never thought possible. It brought us closer than ever.</p>
<p class="abs quote-by">— Marianne, 48</p>

<div class="abs divider" style="top:2913px"></div>

<h2 class="abs ins-title serif">Insights and inspiration discover the path<br>to deeper <em>connection.</em></h2>
<p class="abs ins-lead">We're dedicated to providing insightful content that helps you enhance your relationships.</p>
<article class="abs post" style="left:113px;top:3139px;width:280px">
  <div class="thumb" role="img" aria-label="Woman in a dark blazer among green foliage" style="width:240px;height:214px;background:linear-gradient(160deg,#4d5e3c,#2d2d2d 60%,#6b6b6b)"></div>
  <h4>Building Emotional Intimacy:<br>How to Deepen Your Connection</h4>
  <p>Explore ways to foster meaningful emotional connections with your partner.</p>
  <a class="btn btn-outline" href="#">Read More</a>
</article>
<article class="abs post" style="left:433px;top:3106px;width:332px">
  <div class="thumb" role="img" aria-label="Red-haired woman in a pink jacket outdoors" style="width:332px;height:210px;background:linear-gradient(160deg,#5f7a46,#d9a08e 60%,#b96b4d)"></div>
  <h4>5 Ways to Reignite Passion in<br>Your Relationship</h4>
  <p>Simple yet powerful tips to bring excitement back into your relationship.</p>
  <a class="btn" href="#">Read More</a>
</article>
<article class="abs post" style="left:807px;top:3139px;width:280px">
  <div class="thumb" role="img" aria-label="Blonde woman in a white knit sweater" style="width:242px;height:214px;background:linear-gradient(160deg,#c7c2bb,#efece6 55%,#a59a8c)"></div>
  <h4>The Power of Communication<br>in Intimacy</h4>
  <p>Learn how effective communication can transform your intimate relationship.</p>
  <a class="btn btn-outline" href="#">Read More</a>
</article>

<svg class="abs cta-edge" width="1025" height="20" viewBox="0 0 1025 20"><path d="M0 20V8L40 14 100 4 160 12 230 5 300 13 380 3 450 11 530 6 610 13 690 4 770 12 850 6 930 12 1025 7V20Z" fill="#3e5d5a"/></svg>
<div class="abs cta-panel"></div>
<div class="abs cta-copy">
  <h2 class="serif">Schedule your free consultation today to learn how Moonlit Cadence can <em>help you.</em></h2>
  <a class="btn" href="#" style="font-size:9.5px;padding:10px 24px">Book Your Free 30-Minute Consultation</a>
</div>
<div class="abs cta-photo" role="img" aria-label="Woman with short dark hair in a light blazer against a dark brick wall"></div>

<footer class="abs footer">
  <div class="abs f-col" style="left:110px">
    <div class="brand">Moonlit Cadence</div>
    <div class="socials"><span></span><span></span><span></span><span></span></div>
  </div>
  <div class="abs f-col" style="left:395px">
    <h5>Quick Links</h5>
    <ul><li>Home</li><li>About</li><li>Services</li><li>Contact</li><li>Blog</li></ul>
  </div>
  <div class="abs f-col contact" style="left:585px">
    <h5>Contact Us</h5>
    <ul>
      <li><svg width="9" height="9" viewBox="0 0 10 10"><path d="M2 1l2 2-1 1.5a6 6 0 0 0 2.5 2.5L7 6l2 2-1.5 1.5C4 9 1 6 .5 2.5Z" fill="#fff"/></svg>+ (555) 010 2040</li>
      <li><svg width="9" height="9" viewBox="0 0 10 10" fill="none" stroke="#fff"><rect x="1" y="2" width="8" height="6"/><path d="M1 2l4 3 4-3"/></svg>hello@moonlitcadence.com</li>
      <li><svg width="9" height="9" viewBox="0 0 10 10"><path d="M5 0a3.5 3.5 0 0 0-3.5 3.5C1.5 6 5 10 5 10s3.5-4 3.5-6.5A3.5 3.5 0 0 0 5 0Z" fill="#fff"/></svg><span>214 Willow Lane, Suite 5,<br>Eastbrook, Oregon 97000</span></li>
    </ul>
  </div>
  <div class="abs f-col subscribe" style="left:872px">
    <h5>Subscribe Our Newsletter</h5>
    <p>Unlock 10% off your first subscription when you sign up for our newsletter.</p>
    <div class="sub-field"><span>Enter Email</span><b>→</b></div>
  </div>
  <div class="abs footer-bottom">
    <span><span class="gold">Moonlit Cadence</span> © All Rights Reserved.</span>
    <span>Terms and Conditions &nbsp;&nbsp;&nbsp;&nbsp;&nbsp;&nbsp; Privacy Policy</span>
  </div>
</footer>

</body>
</html>
```